Author needs design for self-help relationship book

I need a book cover design for a self-help handbook on relationships called 'Seven quiet habits for building forever bonds with your partner - fast". The design should appeal in the main to young couples anywhere in the world.

```html
<!DOCTYPE html>
<html lang="en">
<head>
<meta charset="utf-8">
<title>Forever Bonds – Book Cover</title>
<link rel="stylesheet" href="https://fonts.googleapis.com/css2?family=Oswald:wght@600&family=League+Gothic&family=Roboto+Condensed:wght@400&family=Parisienne&display=swap">
<style>
  :root {
    --cream: #fbf3dc;
    --paper-light: #f3e3b4;
    --paper-mid: #cdb27a;
    --sepia-dark: #5a4326;
    --sepia-deep: #3a2a17;
    --maroon: #7a1030;
    --title-ink: #fdf6e6;
  }
  html, body {
    margin: 0;
    padding: 0;
    width: 888px;
    height: 1200px;
    overflow: hidden;
    background: var(--sepia-deep);
  }
  .cover {
    position: relative;
    width: 888px;
    height: 1200px;
    overflow: hidden;
  }
  .cover-photo {
    position: absolute;
    inset: 0;
    background:
      radial-gradient(ellipse 55% 40% at 72% 30%, rgba(120, 88, 50, 0.55), transparent 70%),
      radial-gradient(ellipse 45% 45% at 30% 72%, rgba(60, 42, 24, 0.6), transparent 72%),
      linear-gradient(180deg, var(--paper-light) 0%, var(--paper-light) 30%, var(--paper-mid) 55%, var(--sepia-dark) 85%, var(--sepia-deep) 100%);
  }
  .author-name {
    position: absolute;
    left: 72px;
    top: 58px;
    margin: 0;
    font-family: "Oswald", sans-serif;
    font-weight: 600;
    font-size: 62px;
    line-height: 1;
    letter-spacing: 0.5px;
    color: var(--maroon);
  }
  .title-block {
    position: absolute;
    left: 372px;
    top: 666px;
    width: 480px;
    color: var(--title-ink);
  }
  .title-lead {
    margin: 0 0 6px 2px;
    font-family: "Roboto Condensed", sans-serif;
    font-size: 28px;
    line-height: 1.1;
  }
  .title-main {
    margin: 0;
    font-family: "League Gothic", sans-serif;
    font-weight: 400;
    font-size: 172px;
    line-height: 0.86;
    letter-spacing: 1px;
    text-transform: uppercase;
  }
  .title-main span { display: block; }
  .title-tail {
    margin: 18px 0 0 24px;
    font-family: "Parisienne", cursive;
    font-size: 48px;
    line-height: 1;
  }
</style>
</head>
<body>
  <main class="cover">
    <div class="cover-photo" role="img" aria-label="Sepia-toned photograph of a smiling young couple in profile, the man behind and above the woman, looking out toward a bright horizon"></div>
    <p class="author-name">AUTHOR NAME</p>
    <div class="title-block">
      <p class="title-lead">Seven quiet habits for building</p>
      <h1 class="title-main"><span>Forever</span><span>Bonds</span></h1>
      <p class="title-tail">with your partner – fast</p>
    </div>
  </main>
</body>
</html>
```